Real Estate Website

We currently have an existing site at https://plovermarshdesk.com.au/ but require a much more professional design.

We like the style/design of the following which are competitors : https://tidalquince.com.au/
https://www.ferncaddyhub.com.au/
https://mossylanternco.com.au/

```html
<!DOCTYPE html>
<html lang="en">
<head>
<meta charset="utf-8">
<title>Plover Marsh Desk — Sell and Rent Your Home Yourself</title>
<link rel="stylesheet" href="https://fonts.googleapis.com/css2?family=Mulish:wght@400;600;700&display=swap">
<style>
:root{
  --navy:#231f5c;
  --red:#c9252c;
  --text:#3a3a3a;
  --muted:#6b6b6b;
  --line:#cfcfcf;
  --footer:#232323;
  --footer-text:#b9b9b9;
  --white:#fff;
}
*{box-sizing:border-box;margin:0;padding:0}
html,body{width:1200px;height:3441px;overflow:hidden}
body{font-family:'Mulish',sans-serif;color:var(--text);background:var(--white);position:relative}
.abs{position:absolute}
.btn{position:absolute;background:var(--red);color:var(--white);display:flex;align-items:center;justify-content:center;font-size:16px;border-radius:2px}

/* header */
.brand{left:143px;top:14px;width:140px;text-align:center}
.brand .mark{width:40px;height:40px;border:2px solid var(--red);margin:0 auto 8px;border-radius:50%}
.brand .name{font-size:14px;font-weight:700;color:var(--navy)}
.phone{left:712px;top:24px;font-size:25px;color:var(--text);display:flex;align-items:center;gap:10px}
.login{left:919px;top:23px;width:137px;height:36px;font-size:15px}
.nav{top:76px;font-size:16px;color:var(--text)}

/* hero */
.hero{left:0;top:108px;width:1200px;height:600px}
.hero-title{right:144px;top:272px;text-align:right;font-size:26px;font-weight:600;line-height:35px;color:#1c1c1c;text-transform:uppercase}
.hero-cta{left:943px;top:382px;width:113px;height:39px;font-size:19px;font-weight:700}

/* welcome */
.welcome-title{left:0;width:1200px;top:778px;text-align:center;font-size:34px;color:var(--navy)}
.welcome-text{left:140px;width:920px;top:830px;text-align:center;font-size:16px;line-height:30.5px}
.welcome-btn{left:544px;top:937px;width:112px;height:36px}

/* services */
.services{left:0;top:1069px;width:1200px;height:436px;background:linear-gradient(180deg,#4a4a40 0%,#3e4a35 50%,#54503f 100%)}
.services-title{left:0;width:1200px;top:1148px;text-align:center;font-size:32px;color:var(--white)}
.card{top:1213px;width:433px;height:202px;background:var(--white)}
.card h3{position:absolute;left:145px;top:16px;font-size:21px;font-weight:600;color:var(--red)}
.card p{position:absolute;left:145px;top:50px;width:270px;font-size:11.5px;line-height:22.3px;color:var(--text)}
.card .btn{left:145px;top:148px;width:112px;height:36px}
.card svg{position:absolute;left:30px;top:18px}

/* calculator */
.calc-title{left:0;width:1200px;top:1572px;text-align:center;font-size:34px;line-height:43px;color:var(--navy)}
.label{font-size:12px;color:var(--navy);text-transform:uppercase;line-height:16px}
.select{height:40px;border:1px solid #bdbdbd;background:var(--white);font-size:14.5px;padding-left:15px;display:flex;align-items:center;color:#222}
.select::after{content:"";position:absolute;right:16px;top:14px;width:7px;height:7px;border-right:1.8px solid #333;border-bottom:1.8px solid #333;transform:rotate(45deg)}
.total{left:144px;top:1912px;width:912px;height:40px;background:var(--navy);color:var(--white);font-size:14.5px;padding-left:15px;display:flex;align-items:center}

/* resources */
.resources{left:0;top:2047px;width:1200px;height:603px;background:linear-gradient(90deg,#e4e4e4 0%,#cfd0d0 45%,#bdbdbd 64%,#ececec 66%,#9a9a9a 80%,#dadada 100%)}
.res-title{left:143px;top:2130px;font-size:34px;color:#1f1f1f}
.res-list{left:143px;top:2193px;list-style:none}
.res-list li{font-size:16px;color:var(--navy);line-height:38.4px;display:flex;align-items:center;gap:10px}
.res-list li::before{content:"";width:13px;height:13px;border-radius:50%;background:var(--navy) ;box-shadow:inset 0 0 0 3px var(--navy)}

/* guide */
.guide-title{left:0;width:1200px;top:2740px;text-align:center;font-size:33px;color:#1f1f1f}
.field{border:1px solid #bdbdbd;font-size:12px;color:#555;padding:13px 14px}
.submit{left:544px;top:2981px;width:112px;height:36px;font-size:16px}

/* footer */
.footer{left:0;top:3098px;width:1200px;height:343px;background:var(--footer)}
.f-head{font-size:14.5px;color:var(--footer-text)}
.f-text{font-size:14.5px;color:var(--footer-text);display:flex;align-items:center;gap:18px}
.badge{border-radius:4px;background:#3a3a3a}
.social{width:46px;height:46px;border:1.5px solid #888;border-radius:50%}
.f-rule{left:143px;top:3330px;width:913px;height:1px;background:#4a4a4a}
.f-links{left:143px;top:3362px;font-size:11.5px;color:var(--footer-text);word-spacing:2px}
.f-copy{left:143px;top:3394px;font-size:11.5px;color:var(--footer-text)}
</style>
</head>
<body>

<!-- header -->
<div class="abs brand">
  <div class="mark"></div>
  <div class="name">Plover Marsh Desk</div>
</div>
<div class="abs phone">
  <svg width="18" height="18" viewBox="0 0 24 24"><path fill="#222" d="M6.6 10.8a15 15 0 0 0 6.6 6.6l2.2-2.2a1 1 0 0 1 1-.25 11.4 11.4 0 0 0 3.6.57 1 1 0 0 1 1 1V20a1 1 0 0 1-1 1A17 17 0 0 1 3 4a1 1 0 0 1 1-1h3.5a1 1 0 0 1 1 1c0 1.25.2 2.45.57 3.57a1 1 0 0 1-.25 1z"/></svg>
  1300 481 926
</div>
<div class="btn login">Member Login</div>
<div class="abs nav" style="left:439px">Sell</div>
<div class="abs nav" style="left:507px">Rent</div>
<div class="abs nav" style="left:584px">Add on Services</div>
<div class="abs nav" style="left:745px">Resources</div>
<div class="abs nav" style="left:863px">About Us</div>
<div class="abs nav" style="left:974px">Contact Us</div>

<!-- hero -->
<svg class="abs hero" viewBox="0 0 1200 600" role="img" aria-label="Photo of one hand passing a house key into another open hand">
  <defs>
    <linearGradient id="heroPhoto" x1="0" y1="0" x2="1" y2="0">
      <stop offset="0" stop-color="#c9b9a8"/>
      <stop offset=".4" stop-color="#d9c7b5"/>
      <stop offset=".7" stop-color="#c9d2dc"/>
      <stop offset="1" stop-color="#a9b9cc"/>
    </linearGradient>
  </defs>
  <polygon points="0,0 1200,0 1200,478 600,598 0,478" fill="var(--red)"/>
  <polygon points="0,0 1200,0 1200,466 600,580 0,480" fill="url(#heroPhoto)"/>
  <circle cx="71" cy="253" r="20" fill="#1e1e1e"/>
  <path d="M75 244 l-9 9 9 9" fill="none" stroke="#fff" stroke-width="3"/>
  <circle cx="1127" cy="253" r="20" fill="#1e1e1e"/>
  <path d="M1123 244 l9 9 -9 9" fill="none" stroke="#fff" stroke-width="3"/>
</svg>
<div class="abs hero-title">Help you to sell and rent<br>your home yourself and<br>saving thousands of dollars</div>
<div class="btn hero-cta">LET'S GO</div>

<!-- welcome -->
<h1 class="abs welcome-title" style="font-weight:400">Welcome to Plover Marsh Desk</h1>
<p class="abs welcome-text">Plover Marsh Desk is an Australia real estate expert who can help you to sell, rent &nbsp;your properties yourself and &nbsp;save thousands of dollars at the same time. The owner as traditional agent himself found that the landlord always get charged too much for no matter selling, renting &nbsp;their home by the agents.</p>
<div class="btn welcome-btn">Read More</div>

<!-- services -->
<div class="abs services" role="img" aria-label="Aerial photo of a suburban neighbourhood with houses and lawns"></div>
<h2 class="abs services-title" style="font-weight:400">Services</h2>
<div class="abs card" style="left:144px">
  <svg width="86" height="86" viewBox="0 0 86 86" fill="none" stroke="#222" stroke-width="2.5">
    <path d="M52 10 l22 4 4 22 -40 40 -26 -26z"/>
    <circle cx="64" cy="24" r="5"/>
    <path d="M64 19 q6 -14 14 -8"/>
  </svg>
  <h3>Sale add on</h3>
  <p>Nullam lorem urna, tempus eget mollis et, dapibus ac sem. Suspendisse gravida ornare erat sed pulvinar. Vestibulum luctus ex in egestas fringilla. Fusce nec leo ac urna pulvinar auctor.</p>
  <div class="btn">Read More</div>
</div>
<div class="abs card" style="left:623px">
  <svg width="86" height="86" viewBox="0 0 86 86" fill="none" stroke="#222" stroke-width="2.5">
    <path d="M6 40 L43 8 L80 40"/>
    <path d="M14 34 V78 H72 V34"/>
    <circle cx="43" cy="30" r="4"/>
    <rect x="22" y="50" width="14" height="14"/>
    <rect x="50" y="50" width="14" height="14"/>
    <path d="M38 78 V56 H48 V78"/>
    <path d="M20 20 V6 H28 V14"/>
  </svg>
  <h3>Rental Add on</h3>
  <p>Nullam lorem urna, tempus eget mollis et, dapibus ac sem. Suspendisse gravida ornare erat sed pulvinar. Vestibulum luctus ex in egestas fringilla. Fusce nec leo ac urna pulvinar auctor.</p>
  <div class="btn">Read More</div>
</div>

<!-- calculator -->
<h2 class="abs calc-title" style="font-weight:400">How much could you save by selling with<br>Plover Marsh Desk?</h2>
<div class="abs label" style="left:143px;top:1696px">Property value</div>
<div class="abs label" style="left:374px;top:1696px">Agent commission (%)</div>
<div class="abs label" style="left:606px;top:1696px">Marketing fee ($)</div>
<div class="abs label" style="left:837px;top:1680px;width:220px">Estimated total spend with agent ($)</div>
<div class="abs select" style="left:143px;top:1720px;width:219px">$ 700000</div>
<div class="abs select" style="left:374px;top:1720px;width:219px">+ 2.05</div>
<div class="abs select" style="left:606px;top:1720px;width:219px">+ 5000</div>
<div class="abs select" style="left:837px;top:1720px;width:219px">= 19350</div>
<div class="abs label" style="left:143px;top:1792px">Select our package</div>
<div class="abs select" style="left:143px;top:1816px;width:913px">Basic ($499)</div>
<div class="abs label" style="left:143px;top:1888px">Total saving with our package</div>
<div class="abs total">18851</div>

<!-- resources -->
<div class="abs resources" role="img" aria-label="Photo of a brass door handle with a key and house keyring in a bright room"></div>
<h2 class="abs res-title" style="font-weight:400">Useful Resources</h2>
<ul class="abs res-list">
  <li>General Guide: How to sell home yourself (without an agent)</li>
  <li>General guide: How to rent and manage home yourself</li>
  <li>How to sell home yourself (without an agent) in northern Territory</li>
  <li>How to sell home yourself (without an agent) in ACT</li>
  <li>How to sell home yourself (without an agent) in Tasmania</li>
  <li>How to sell home yourself (without an agent) in SA</li>
  <li>How to Sell home yourself (without an agent) in WA</li>
  <li>How to sell home yourself (without an agent) in VIC</li>
  <li>How to sell home yourself (without an agent) in QLD</li>
  <li>How to Sell home yourself (without an agent) in NSW</li>
</ul>

<!-- guide form -->
<h2 class="abs guide-title" style="font-weight:400">Free E-Guide for selling/renting your property</h2>
<div class="abs field" style="left:264px;top:2806px;width:328px;height:40px">Name</div>
<div class="abs field" style="left:607px;top:2806px;width:328px;height:40px">Email</div>
<div class="abs field" style="left:264px;top:2864px;width:671px;height:96px">Message</div>
<div class="btn submit">Submit</div>

<!-- footer -->
<div class="abs footer"></div>
<div class="abs f-head" style="left:143px;top:3142px">Plover Marsh Desk helps you to list on</div>
<div class="abs badge" style="left:143px;top:3172px;width:206px;height:32px"></div>
<div class="abs badge" style="left:143px;top:3228px;width:137px;height:34px"></div>
<div class="abs f-head" style="left:143px;top:3279px;font-size:14px">+ more sites</div>
<div class="abs f-head" style="left:547px;top:3142px">Contact</div>
<div class="abs f-text" style="left:547px;top:3182px">
  <svg width="13" height="13" viewBox="0 0 24 24"><path fill="#b9b9b9" d="M6.6 10.8a15 15 0 0 0 6.6 6.6l2.2-2.2a1 1 0 0 1 1-.25 11.4 11.4 0 0 0 3.6.57 1 1 0 0 1 1 1V20a1 1 0 0 1-1 1A17 17 0 0 1 3 4a1 1 0 0 1 1-1h3.5a1 1 0 0 1 1 1c0 1.25.2 2.45.57 3.57a1 1 0 0 1-.25 1z"/></svg>
  1300481926
</div>
<div class="abs f-text" style="left:547px;top:3221px">
  <svg width="14" height="11" viewBox="0 0 14 11"><rect width="14" height="11" fill="#b9b9b9"/><path d="M0 0 L7 6 L14 0" fill="none" stroke="#232323" stroke-width="1.4"/></svg>
  info@plovermarshdesk.com.au
</div>
<div class="abs f-head" style="left:941px;top:3142px">Follow us on</div>
<div class="abs social" style="left:943px;top:3177px"></div>
<div class="abs social" style="left:1006px;top:3177px"></div>
<div class="abs f-rule"></div>
<div class="abs f-links">Home &nbsp;| &nbsp;Sell &nbsp;| &nbsp;Rent &nbsp;| &nbsp;Add on Services &nbsp;| &nbsp;Resources &nbsp;| &nbsp;About Us &nbsp;| &nbsp;Contact Us</div>
<div class="abs f-copy">Copyright © 2021 &nbsp;Plover Marsh Desk. &nbsp;All rights reserved. &nbsp;&nbsp;Terms of Use &nbsp;| &nbsp;Privacy Policy</div>
<svg class="abs" style="left:1027px;top:3371px" width="28" height="28" viewBox="0 0 28 28"><circle cx="14" cy="14" r="14" fill="#bdbdbd"/><path d="M8 17 l6 -6 6 6" fill="none" stroke="#232323" stroke-width="3"/></svg>
<div class="abs" style="left:1111px;top:3366px;width:48px;height:48px;border-radius:50%;background:#2f7bf6"></div>
</body>
</html>
```